Looking for potential sellers

We help people buy and sell homes and are currently looking for potential home sellers. We offer low commissions, are the Local Colorado Springs and Falcon Experts, homes selling fast and at top dollar, Free expert pricing opinions and Consultations, over 9 years of experience, top rated Realtors creative and aggressive marketing strategies. Never merely own a house, THRIVE at Harborview. phone number 482-630-9157 web thriveatharborview.com

```html
<!DOCTYPE html>
<html lang="en">
<head>
<meta charset="utf-8">
<title>Harborview Realty – Seller Postcard</title>
<link href="https://fonts.googleapis.com/css2?family=Poppins:wght@400;500;600;700;800&display=swap" rel="stylesheet">
<style>
  :root{
    --stage:#ececec;
    --olive:#a9a862;
    --olive-soft:#b5b26c;
    --charcoal:#363b42;
    --gold-text:#bdb56f;
    --taupe:#a48f7b;
    --white:#ffffff;
    --rule:#c9c9c9;
  }
  *{box-sizing:border-box;margin:0;padding:0}
  html,body{width:1200px;height:960px;overflow:hidden}
  body{background:var(--stage);font-family:"Poppins",sans-serif;position:relative}

  .postcard{position:absolute;left:264px;width:672px;height:448px;overflow:hidden;box-shadow:0 6px 18px rgba(0,0,0,.18)}
  .postcard--front{top:20px;background:var(--charcoal)}
  .postcard--back{top:492px;background:var(--white)}

  /* FRONT */
  .front-art{position:absolute;inset:0}
  .brand{position:absolute;display:flex;align-items:center;gap:8px;color:var(--white);font-weight:600}
  .brand__mark{width:12px;height:12px;background:var(--white)}
  .brand--front{left:30px;top:40px;font-size:22px}
  .headline{position:absolute;left:28px;top:100px;width:230px;color:var(--white);font-size:28px;font-weight:700;line-height:1.18}
  .headline-rule{position:absolute;left:28px;top:192px;width:226px;height:2px;background:var(--white)}
  .intro{position:absolute;left:28px;top:202px;width:228px;color:var(--white);font-size:8.6px;line-height:1.5}
  .site-url{position:absolute;right:22px;top:22px;color:var(--white);font-size:14px;font-weight:600}

  .features{position:absolute;left:28px;top:302px;width:620px;display:flex}
  .feature{display:flex;align-items:center;gap:12px}
  .feature:nth-child(1){width:176px}
  .feature:nth-child(2){width:200px}
  .feature__icon{width:38px;height:38px;background:var(--olive);display:flex;align-items:center;justify-content:center}
  .feature__label{font-size:13px;font-weight:600;line-height:1.25;text-transform:uppercase;color:var(--white)}
  .feature__label span{display:block;color:var(--gold-text)}

  .details{position:absolute;left:28px;top:370px;width:620px;display:flex;align-items:center;color:var(--white);font-size:11.5px;line-height:1.4}
  .details__item:nth-child(1){width:166px}
  .details__divider{width:1px;height:30px;background:var(--white);margin:0 14px}
  .details__item--cta{width:230px}
  .details__phone{display:block;font-weight:600}
  .band-stripe{position:absolute;left:0;right:0;bottom:0;height:14px;background:var(--olive)}

  /* BACK */
  .back-panel{position:absolute;inset:0}
  .back-title{position:absolute;left:28px;top:22px;color:var(--white);font-size:24px;font-weight:800}
  .back-tagline{position:absolute;left:28px;top:58px;color:var(--white);font-size:10.5px;font-weight:600}
  .back-copy{position:absolute;left:28px;top:76px;width:320px;color:var(--white);font-size:8.8px;line-height:1.5}
  .agent-photo{position:absolute;left:30px;top:234px;width:200px;height:214px;background:linear-gradient(180deg,#b7a48f 0%,#8f7a66 45%,#3a3a40 100%)}
  .back-contact{position:absolute;left:240px;top:300px;width:140px;color:var(--white)}
  .brand--back{position:static;font-size:18px;margin-bottom:14px}
  .back-contact__lead{font-size:11px;font-weight:700}
  .back-contact__phone{font-size:17px;font-weight:700;letter-spacing:1px}
  .back-contact__url{font-size:10px;font-weight:700}
  .address-lines{position:absolute;left:430px;top:190px;width:200px}
  .address-lines span{display:block;height:1px;background:var(--rule);margin-bottom:28px}
</style>
</head>
<body>

<section class="postcard postcard--front">
  <svg class="front-art" width="672" height="448" viewBox="0 0 672 448">
    <defs>
      <linearGradient id="scene" x1="0" y1="0" x2="0" y2="1">
        <stop offset="0" stop-color="#4a3d52"/>
        <stop offset=".28" stop-color="#b0675e"/>
        <stop offset=".45" stop-color="#7c7484"/>
        <stop offset=".62" stop-color="#2f3a2c"/>
        <stop offset="1" stop-color="#1f2a1e"/>
      </linearGradient>
    </defs>
    <polygon points="0,0 255,0 325,285 0,285" fill="var(--olive)"/>
    <polygon points="255,0 672,0 672,285 325,285" fill="url(#scene)" role="img" aria-label="Mountain lake landscape at sunset"/>
  </svg>

  <div class="brand brand--front"><span class="brand__mark"></span>Harborview</div>
  <h1 class="headline">Looking to Sell Your Home?</h1>
  <div class="headline-rule"></div>
  <p class="intro">There's never been a better time to sell your home in Colorado Springs! With home values rising almost 10% in the last year alone, and predicted to jump another 3.7% within the year, it truly is a seller's market!</p>
  <div class="site-url">thriveatharborview.com</div>

  <div class="features">
    <div class="feature">
      <div class="feature__icon">
        <svg width="22" height="22" viewBox="0 0 22 22" fill="none" stroke="#fff" stroke-width="1.6">
          <line x1="6" y1="12" x2="16" y2="2"/><circle cx="6" cy="4" r="1.8"/><circle cx="16" cy="10" r="1.8"/>
          <polyline points="4,15 11,21 18,15"/>
        </svg>
      </div>
      <div class="feature__label">Low<span>Commissions</span></div>
    </div>
    <div class="feature">
      <div class="feature__icon">
        <svg width="24" height="22" viewBox="0 0 24 22" fill="none" stroke="#fff" stroke-width="1.6">
          <polyline points="9,3 16,11 9,19"/><polyline points="15,3 22,11 15,19"/>
          <text x="1" y="15" fill="#fff" stroke="none" font-size="11" font-family="Poppins,sans-serif">$</text>
        </svg>
      </div>
      <div class="feature__label">Fast selling and<span>at top dollar</span></div>
    </div>
    <div class="feature">
      <div class="feature__icon">
        <svg width="24" height="22" viewBox="0 0 24 22" fill="#fff">
          <circle cx="8" cy="6" r="3"/><path d="M2 16c0-4 3-6 6-6s6 2 6 6z"/>
          <circle cx="17" cy="10" r="2.6"/><path d="M12 21c0-3 2.5-5 5-5s5 2 5 5z"/>
        </svg>
      </div>
      <div class="feature__label">Free expert pricing<span>consultations</span></div>
    </div>
  </div>

  <div class="details">
    <p class="details__item">Over 9 years of experience, top rated Realtors</p>
    <span class="details__divider"></span>
    <p class="details__item details__item--cta">Ready to make a change? Contact us to sell your property today!</p>
    <span class="details__divider"></span>
    <p class="details__item">Get in touch with us<span class="details__phone">482-630-9157</span></p>
  </div>
  <div class="band-stripe"></div>
</section>

<section class="postcard postcard--back">
  <svg class="back-panel" width="672" height="448" viewBox="0 0 672 448">
    <polygon points="0,0 370,0 390,448 0,448" fill="var(--taupe)"/>
  </svg>
  <h2 class="back-title">It's Time...</h2>
  <p class="back-tagline">Never merely own a house, THRIVE at Harborview.</p>
  <p class="back-copy">Harborview Realty and our lead broker Dale Morgan have been helping clients find their dream homes in beautiful Colorado Springs and its surrounding areas for years. We know that buying or selling your home can be one of the most exciting (and sometimes trying) times of your life. Because of this, we make a concerted effort to know and understand your wants and needs, which plays a crucial part in both your success and ours.</p>
  <div class="agent-photo" role="img" aria-label="Portrait of the lead broker"></div>
  <div class="back-contact">
    <div class="brand brand--back"><span class="brand__mark"></span>Harborview</div>
    <p class="back-contact__lead">Get in touch with us</p>
    <p class="back-contact__phone">482-630-9157</p>
    <p class="back-contact__url">thriveatharborview.com</p>
  </div>
  <div class="address-lines"><span></span><span></span><span></span><span></span></div>
</section>

</body>
</html>
```